Tri-Fold Brochure for Transportation Equipment Dealer

We need a design of a new tri-fold brochure for our company. This is what we give to customers and prospective customers. Many of our customers do not know the diversity of our product line and capabilities. We have a lot of information to share with them in a small package. I have provided a draft of the content that I wanted included (in a .pptx and .pdf format), but we need it enhanced with color and made to look more professional. We need it to be informative yet professional.

Target Market(s)

Transportation industry customers. Fleet carriers and owner/operator truck drivers.

Industry/Entity Type

Truck Service

Font styles to use
Serif
Sans Serif

Colors
3176b5

Requirements
Must have
• Color. Must include the information that I have provided in the draft. Must be US Letter size.
Nice to have
• Color and separation of different sections.

```html
<!DOCTYPE html>
<html lang="en">
<head>
<meta charset="utf-8">
<title>Coastline Pneumatic Tri-Fold Brochure</title>
<link rel="stylesheet" href="https://fonts.googleapis.com/css2?family=Open+Sans:wght@400;600;700&family=Noto+Serif:wght@700&display=swap">
<style>
:root{
  --blue:#3176b5;
  --navy:#1f4f86;
  --ink:#2b2b2b;
  --black:#0d0d0d;
  --panel:#f2f3f5;
  --panel-dark:#e8eaed;
  --rule:#b9bec5;
  --white:#ffffff;
  --page:#e4e5e7;
}
*{box-sizing:border-box;margin:0;padding:0}
html,body{width:1200px;height:1200px;overflow:hidden}
body{background:var(--page);font-family:"Open Sans",Arial,sans-serif;color:var(--ink);display:flex;flex-direction:column;align-items:center;justify-content:center;gap:18px}
.spread{width:740px;height:572px;display:grid;grid-template-columns:repeat(3,1fr);background:var(--panel);box-shadow:0 2px 8px rgba(0,0,0,.18);position:relative}
.panel{position:relative;overflow:hidden;display:flex;flex-direction:column}
.photo{background:linear-gradient(135deg,#c9ced5,#8d96a1);border-radius:2px}
.photo.round{border-radius:50%}
.photo.dark{background:linear-gradient(160deg,#2c3a4e,#101824)}
.photo.warm{background:linear-gradient(135deg,#9aa3ad,#5d6670)}
.cap{font-size:7px;color:var(--blue);text-align:center;margin-top:2px}
.cap.bold{font-weight:700;color:var(--ink)}

/* outside: services */
.services{padding:12px 14px 0}
.services h2{color:var(--blue);font-size:21px;font-weight:700;letter-spacing:.5px}
.brand-name{font-weight:700;font-size:15px;color:var(--ink);line-height:1}
.brand-sub{font-size:5.5px;letter-spacing:1px;color:#666;margin-top:3px}
.svc-row{display:flex;gap:8px;align-items:center;font-size:8px;line-height:1.25}
.svc-block{border-bottom:1px solid var(--blue);padding:8px 0}
.svc-block:last-child{border:none}

/* outside: locations */
.locations{background:var(--blue);color:var(--white)}
.loc-head{background:var(--black);height:166px;padding:10px 12px;display:grid;grid-template-columns:1fr 64px;gap:6px}
.loc-title{display:flex;align-items:center;gap:4px;justify-content:center}
.loc-title .num{font-size:38px;line-height:1}
.loc-title .lines{font-size:13px;line-height:1.1}
.loc-title b{font-weight:700}
.map{height:78px;margin:6px 0 4px;background:linear-gradient(90deg,#c8242b 0 38%,#f5f5f5 38% 52%,var(--blue) 52%)}
.loc-url{font-family:"Noto Serif",Georgia,serif;font-size:10px;text-align:center}
.hours{border-left:1px solid var(--blue);padding-left:7px;font-size:9px;margin-top:46px}
.hours h4{color:var(--blue);font-size:11px;line-height:1.05;margin-bottom:14px}
.hours p{line-height:1.15;margin-bottom:9px}
.addr{padding:8px 42px 0;text-align:center;font-size:5.6px;line-height:1.35}
.addr h5{font-size:8.5px;font-weight:700;line-height:1.15}
.addr h5 span{font-weight:400;display:block}
.addr .group{border-bottom:1px solid rgba(255,255,255,.7);padding-bottom:6px;margin-bottom:6px}
.addr .group:last-child{border:none}
.addr p{margin-top:5px}

/* outside: cover */
.cover{background:var(--white);align-items:center;padding-top:18px}
.cover-name{font-size:28px;font-weight:700;color:var(--blue);line-height:1}
.cover-sub{font-size:10.5px;color:#777;text-align:center;line-height:1.25;margin-top:10px}
.cover-stack{width:154px;height:236px;background:var(--panel-dark);margin-top:28px;padding:6px;display:grid;grid-template-rows:1fr 1fr 1fr;gap:6px}
.cover-stack .pair{display:grid;grid-template-columns:1fr 1fr;gap:6px}
.tagline{width:100%;text-align:center;margin-top:44px;color:var(--blue);font-weight:700;font-size:18px;line-height:1.05}
.tagline .light{font-weight:400}
.tagline .band{background:var(--navy);color:var(--white);display:block;padding:1px 0}
.cover-cats{font-size:11px;color:#666;margin-top:7px}
.cover-phone{font-size:12.5px;font-weight:700;margin-top:14px}
.cover-url{font-size:9.5px}

.foot{position:absolute;left:0;bottom:0;width:66.67%;height:50px;background:var(--white);display:grid;grid-template-columns:1fr 1fr}
.foot-brand{display:flex;align-items:center;gap:10px;padding-left:40px}
.foot-brand b{color:var(--blue);font-size:13px;font-weight:700}
.foot-brand span{font-size:7px;line-height:1.2}
.foot-online{display:flex;align-items:center;gap:10px;padding-left:30px}
.foot-online b{color:var(--blue);font-size:11px;line-height:1}
.foot-online .rule{width:1px;height:30px;background:var(--ink)}
.foot-online span{font-size:7px;line-height:1.7}

/* inside */
.inside .panel{padding:14px 14px 0}
.inside h3{font-weight:400;font-size:17px;text-align:center;border-bottom:3px solid var(--rule);padding-bottom:3px;margin-bottom:14px}
.rank{display:flex;align-items:flex-start;gap:6px;color:var(--blue);padding-left:2px}
.rank .big{font-size:36px;font-weight:700;line-height:1}
.rank .usa{font-size:24px;font-weight:700;line-height:1}
.rank .usa span{display:block;font-size:13px;font-weight:400}
.years{display:flex;align-items:center;gap:12px;font-size:11px;margin:10px 0 12px 26px}
.blower-brand{display:flex;justify-content:space-between;align-items:center;margin-bottom:6px}
.blower-brand b{font-size:20px;font-weight:700;line-height:1}
.blue-box{background:var(--blue);color:var(--white);font-size:9px;line-height:1.2;margin:0 -14px;padding:10px 14px}
.blue-box p+p{margin-top:10px}
.photo-grid{display:grid;grid-template-columns:1fr 1fr;gap:4px 16px;margin-top:10px}
.photo-grid .photo{height:60px}
.trailer-grid{display:grid;grid-template-columns:1fr 1fr;gap:10px 8px}
.trailer-grid .photo{height:58px}
.stock-box{background:var(--navy);color:var(--white);text-align:center;font-size:11.5px;line-height:1.35;padding:6px 4px;margin:24px 0 14px}
.stock-box b{font-weight:700}
.small{font-size:9px;line-height:1.25;margin-bottom:14px}
.rep{color:var(--blue);text-align:center;font-size:11px;line-height:1.3}
.badges{display:flex;justify-content:space-between;align-items:center;margin-top:12px}
.badges i{display:block;width:38px;height:14px;background:#999;border-radius:2px}
.badges i:first-child{width:16px;height:18px}
.parts{background:var(--panel-dark)}
.parts-head{font-size:20px;line-height:1.25}
.parts-head b{color:var(--blue);font-weight:700}
.tiles{display:grid;grid-template-columns:repeat(3,1fr);gap:14px 10px;margin-top:16px}
.tile{display:flex;flex-direction:column}
.tile .photo{height:42px;background:linear-gradient(135deg,#fff,#c9ced5)}
.tile span{background:var(--blue);color:var(--white);font-size:7px;text-align:center;line-height:1.1;padding:3px 1px;min-height:20px;display:flex;align-items:center;justify-content:center}
.tile.center{grid-column:2}
.warehouse{position:absolute;left:0;bottom:0;width:100%;height:180px}
</style>
</head>
<body>

<section class="spread outside">
  <div class="panel services">
    <h2>SERVICES</h2>
    <div class="svc-block">
      <div class="svc-row">
        <div style="flex:1">
          <div class="brand-name">Ardent Blower</div>
          <div class="brand-sub">AUTHORIZED DISTRIBUTOR</div>
          <p style="margin-top:22px">All of our facilities (except Miami) offer full service installation and repair services</p>
        </div>
        <div>
          <div class="photo round" style="width:84px;height:84px;background:radial-gradient(#f2c230,#6e6a5e)" role="img" aria-label="Dump trailer with liner"></div>
          <div class="cap">Liners</div>
        </div>
      </div>
    </div>
    <div class="svc-block">
      <div class="svc-row">
        <div>
          <div class="photo round warm" style="width:84px;height:84px" role="img" aria-label="Truck-mounted PTO blower"></div>
          <div class="cap" style="font-weight:700">PTO Blowers</div>
        </div>
        <p style="flex:1">Including sandblasting, preventative maint, custom fabrication and DOT services</p>
      </div>
    </div>
    <div class="svc-block" style="font-size:8px;line-height:1.25">
      <p>Blower service &amp; oil change, vacuum pumps, liquid pumps, hydraulic systems, hydraulic coolers, wet line kits, tarps, liner, live floors, automated manways.</p>
      <div class="cap" style="font-weight:700;margin:10px 0 4px">Wreck Repair</div>
      <div style="display:grid;grid-template-columns:84px 1fr;gap:10px;align-items:center">
        <div><div class="photo round warm" style="height:84px" role="img" aria-label="Damaged trailer before repair"></div><div class="cap bold">Before</div></div>
        <div><div class="photo" style="height:70px" role="img" aria-label="Repaired tank trailer"></div><div class="cap bold">After</div></div>
      </div>
    </div>
  </div>

  <div class="panel locations">
    <div class="loc-head">
      <div>
        <div class="loc-title"><span class="num">7</span><span class="lines">Locations<br><b>to Serve You</b></span></div>
        <div class="map" role="img" aria-label="Map of the United States showing branch regions"></div>
        <div class="loc-url">www.bulkhaulgear.com</div>
      </div>
      <div class="hours">
        <h4>Facility Hours</h4>
        <p>Monday<br>Friday</p>
        <p>8:00 AM<br>5:00 PM</p>
      </div>
    </div>
    <div class="addr">
      <div class="group">
        <h5>Coastline<span>Pneumatic</span></h5>
        <p>410 Pine Ridge Rd: HQ, Blower Shop<br>92 Mill Creek St: Trailer Shop, Sales<br>Oakmont, GA 30900<br>800-555-0148<br>sales.east@bulkhaulgear.com</p>
        <p>7200 County Rd 14<br>Brookhaven, NC 27000<br>866-555-0133<br>sales.brookhaven@bulkhaulgear.com</p>
      </div>
      <div class="group">
        <h5>Harbor Pneumatic<span style="font-weight:700">Exports</span></h5>
        <p>1840 Harbor Blvd<br>Bayview, FL 33100<br>888-555-0172<br>sales.harbor@bulkhaulgear.com</p>
      </div>
      <div class="group">
        <h5>Mesa<span>Pneumatic</span></h5>
        <p>18500 Route 81<br>Elm Springs, TX 78600<br>800-555-0191<br>sales.mesa@bulkhaulgear.com</p>
        <p>6610 Dock St<br>Portside, TX 77000<br>866-555-0164<br>sales.portside@bulkhaulgear.com</p>
        <p>2940 Ranch Rd<br>Cedar Flats, TX 76000<br>866-555-0187<br>sales.cedar@bulkhaulgear.com</p>
      </div>
    </div>
  </div>

  <div class="panel cover">
    <div class="cover-name">Coastline</div>
    <div class="cover-sub">Coastline Pneumatic<br>Mesa Pneumatic<br>Harbor Pneumatic Exports</div>
    <div class="cover-stack">
      <div><div class="photo" style="height:64px" role="img" aria-label="Pneumatic tank trailer"></div><div class="cap" style="color:var(--ink);text-align:right">Pneumatics</div></div>
      <div><div class="photo" style="height:64px" role="img" aria-label="End dump trailer"></div><div class="cap" style="color:var(--ink);text-align:right">End Dump</div></div>
      <div class="pair">
        <div><div class="photo" style="height:56px" role="img" aria-label="Electric blower unit"></div><div class="cap" style="color:var(--ink)">Electric</div></div>
        <div><div class="photo" style="height:56px" role="img" aria-label="Diesel blower unit"></div><div class="cap" style="color:var(--ink)">Diesel</div></div>
      </div>
    </div>
    <div class="tagline">EXPERTS <span class="light">IN</span><span class="band">DRY BULK<br>TRANSPORTATION</span>SOLUTIONS</div>
    <div class="cover-cats">New | Used | Services | Parts</div>
    <div class="cover-phone">800-555-0148</div>
    <div class="cover-url">www.bulkhaulgear.com</div>
  </div>

  <div class="foot">
    <div class="foot-brand"><b>Coastline</b><span>Coastline Pneumatic<br>Mesa Pneumatic<br>Harbor Pneumatic Exports</span></div>
    <div class="foot-online"><b>Find us<br>online</b><div class="rule"></div><span>Coastline Pneumatic, Inc.<br>@bulkhaulgear</span></div>
  </div>
</section>

<section class="spread inside">
  <div class="panel">
    <h3>Blowers</h3>
    <div class="rank"><span class="big">#1</span><span class="usa">USA<span>mobile blower distributor</span></span></div>
    <div class="years"><div class="photo" style="width:22px;height:30px;background:linear-gradient(#f4cc2a,#c99a10)" role="img" aria-label="Award trophy"></div>2014 - 2015 - 2016 - 2017</div>
    <div class="blower-brand"><b>Ardent Blower</b><div class="photo" style="width:78px;height:54px;background:linear-gradient(135deg,#d23a44,#7a1b22)" role="img" aria-label="Red mobile blower unit"></div></div>
    <div class="blue-box">
      <p>We are proud to represent the Ardent Blower line of mobile products for use in dry bulk liquid and hydraulic applications. Ardent Blower blowers are the most efficient and productive blowers on the market.</p>
      <p>We specialize in blower installations for your trailer or truck. With our expertise and several model designs we can meet any mounting arrangement or need.</p>
      <p>We can integrate your system with hydraulics as well as power take off units (PTO).</p>
    </div>
    <div class="photo-grid">
      <div><div class="photo" role="img" aria-label="Blowers in stock"></div><div class="cap bold">Stock</div></div>
      <div><div class="photo warm" role="img" aria-label="Technician repairing a blower"></div><div class="cap bold">Repair</div></div>
      <div><div class="photo" style="background:linear-gradient(135deg,#fff,#8a7a60)" role="img" aria-label="PTO kit components"></div><div class="cap bold">PTO Kits</div></div>
      <div><div class="photo warm" role="img" aria-label="Packaged blower units in shop"></div><div class="cap bold">Package Units</div></div>
    </div>
  </div>

  <div class="panel">
    <h3>Trailers</h3>
    <div class="trailer-grid">
      <div><div class="photo" role="img" aria-label="Vacuum pneumatic tank trailer"></div><div class="cap">Vacuum Pneumatic</div></div>
      <div><div class="photo" role="img" aria-label="Hopper trailer"></div><div class="cap">Hopper</div></div>
      <div><div class="photo" role="img" aria-label="Dry bulk pneumatic trailer"></div><div class="cap">Dry Bulk Pneumatic</div></div>
      <div><div class="photo" style="background:linear-gradient(#f2f3f5 40%,#222 40% 60%,#f2f3f5 60%)" role="img" aria-label="Lowboy trailer"></div><div class="cap">Lowboys<br>www.primelowbeds.com</div></div>
      <div><div class="photo" role="img" aria-label="End dump trailer"></div><div class="cap">End Dump</div></div>
      <div><div class="photo warm" role="img" aria-label="Belt trailer"></div><div class="cap">Belt</div></div>
    </div>
    <div class="stock-box">Check out<br>our current stock and inventory at:<br><b>www.bulkhaulgear.com/inventory</b></div>
    <p class="small">We can custom configure your trailer to meet your requirements</p>
    <p class="small">We have the ability to do after-factor modifications to your specs</p>
    <div class="rep">Brand<br>We Represent</div>
    <div class="badges"><i></i><i></i><i></i><i></i><i></i></div>
  </div>

  <div class="panel parts">
    <h3>Parts</h3>
    <p class="parts-head">99% of parts in stock<br><b>ship within 24 hours</b><br>of receipt of order</p>
    <div class="tiles">
      <div class="tile"><div class="photo" role="img" aria-label="Hydraulic and wet line kit parts"></div><span>Hydraulic<br>&amp; Wet Line Kits</span></div>
      <div class="tile"><div class="photo" role="img" aria-label="Assorted trailer parts"></div><span>Trailer Parts</span></div>
      <div class="tile"><div class="photo" role="img" aria-label="Filter and precleaner"></div><span>Filter<br>&amp; Precleaner</span></div>
      <div class="tile"><div class="photo" role="img" aria-label="PTO units"></div><span>PTO</span></div>
      <div class="tile"><div class="photo" role="img" aria-label="Hoses and fittings"></div><span>Hose &amp; Fittings</span></div>
      <div class="tile"><div class="photo" role="img" aria-label="Valves and fittings"></div><span>Valves<br>&amp; Fittings</span></div>
      <div class="tile center"><div class="photo" role="img" aria-label="Vacuum pump"></div><span>Vacuum Pump</span></div>
    </div>
    <div class="photo dark warehouse" role="img" aria-label="Parts warehouse shelving"></div>
  </div>
</section>

</body>
</html>
```